Oak Harbor Interiors Web Site

We are looking at web site for our start-up company which is located in Abu Dhabi United Arab Emirates. Our main business activity is Interior fit out for high medium to high end projects in residential, corporate and hospitality.
In terms of look and feel the web site should be vibrant yet professional reflecting the artistic/construction nature of our business and built along or allows the following aspects:
- Number of Pages: 8-10 main pages (Including 10 Sub Pages)
- A custom responsive web design compatible with all browsers
- Dynamic (admin panel). CMS
- Anti Spam Online Forms
- Photo & Video Gallery
- Mobile Ready (Iphone,Android)]
- Social Media Integration
- Google Map
- Banner Artworks

```html
<!DOCTYPE html>
<html lang="en">
<head>
<meta charset="utf-8">
<title>Oak Harbor Interiors</title>
<link href="https://fonts.googleapis.com/css2?family=Open+Sans:ital,wght@0,400;0,600;0,700;1,400&family=Raleway:wght@400;700&display=swap" rel="stylesheet">
<style>
:root{
  --teal-dark:#1c4257;
  --teal:#1aa6c6;
  --ink:#2a2a2a;
  --text-grey:#8a8a8a;
  --band-dark:#3b3b3b;
  --band-mid:#5a5a5a;
  --light:#f1f1f1;
  --footer:#2c2c2c;
  --footer-bottom:#222;
  --footer-text:#8d8d8d;
  --white:#fff;
}
*{margin:0;padding:0;box-sizing:border-box}
html,body{width:1200px;height:1000px;overflow:hidden;background:var(--white)}
body{position:relative;font-family:"Open Sans",Arial,sans-serif;color:var(--ink)}
.abs{position:absolute}

/* header */
.top-rule{left:0;top:0;width:1200px;height:2px;background:var(--teal-dark)}
.brand{left:0;top:14px;width:1200px;display:flex;justify-content:center;align-items:center;gap:10px}
.brand-mark{width:26px;height:26px;background:var(--teal-dark)}
.brand-name{font-family:"Raleway",sans-serif;font-weight:400;font-size:21px;color:#2a3a44;letter-spacing:.5px}

/* hero band */
.hero-band{left:0;top:65px;width:1200px;height:167px;background:radial-gradient(ellipse at center,var(--band-mid),var(--band-dark) 75%)}
.nav{left:134px;top:74px;width:904px;height:19px;background:var(--white);display:flex;align-items:center;font-size:7px;font-weight:700;letter-spacing:.4px;color:#333}
.nav a{color:inherit;text-decoration:none;padding:0 20px;height:19px;line-height:19px}
.nav a.active{background:var(--teal-dark);color:var(--white);padding:0 16px}
.nav .cart{display:flex;align-items:center;gap:12px}
.search-btn{left:1040px;top:74px;width:35px;height:19px;background:var(--teal-dark);display:flex;align-items:center;justify-content:center}
.slider{left:134px;top:103px;width:942px;height:147px;background:linear-gradient(180deg,var(--teal) 0,#1797b6 82%,#e8e8e8 82%,#f4f4f4 100%)}
.slider-title{left:247px;top:158px;font-family:"Raleway",sans-serif;font-weight:700;font-size:21px;color:var(--white);letter-spacing:.5px}
.slider-sub{left:248px;top:182px;font-size:9px;color:var(--white)}
.slider-dots{left:548px;top:226px;display:flex;gap:3px}
.slider-dots span{width:10px;height:10px;border-radius:50%;border:1px solid #666;background:#eee}
.slider-dots span.on{background:#444}

/* intro */
.intro{left:130px;top:268px;width:940px;text-align:center;font-weight:700;font-size:15.5px;line-height:18px;color:var(--ink)}

/* features */
.feature{top:321px;width:280px;text-align:center}
.feature-badge{width:110px;height:42px;border-radius:50%;background:var(--teal-dark);margin:0 auto;display:flex;align-items:center;justify-content:center}
.feature h3{font-size:9.5px;font-weight:700;margin-top:6px;color:var(--ink)}
.feature p{font-size:7.5px;line-height:10px;color:var(--text-grey);margin-top:1px;padding:0 8px}
.btn{display:inline-block;background:var(--teal-dark);color:var(--white);font-size:7.5px;height:13px;line-height:13px;border-radius:2px}
.feature .btn{width:86px;margin-top:6px}
.btn-dark{background:#333;width:82px;text-align:center}

/* section headings */
.section-title{font-size:9px;font-weight:700;color:var(--ink);letter-spacing:.2px}
.section-title em{font-style:normal;color:var(--teal-dark)}

/* news */
.news-item{left:134px;width:290px;height:24px;display:flex;gap:17px}
.thumb{width:52px;height:18px;background:linear-gradient(90deg,#b5a48d,#e6e1d9)}
.news-item h4{font-size:7.5px;font-weight:700;line-height:8px}
.news-item p{font-size:7.5px;line-height:9px;color:var(--text-grey)}

/* gallery */
.gallery{left:474px;top:485px;display:grid;grid-template-columns:repeat(4,143px);grid-auto-rows:43px;column-gap:10px;row-gap:4px}
.gallery div{border-radius:2px}

/* testimonial & partners */
.testimonial-photo{left:145px;top:679px;width:63px;height:24px;background:linear-gradient(90deg,#d8d2cb,#b8a394)}
.quote{left:228px;top:679px;width:358px;height:36px;background:#ececec;padding:5px 14px;font-style:italic;font-size:7.5px;line-height:9px;color:#4a6b80}
.quote-author{left:230px;top:717px;font-style:italic;font-weight:600;font-size:8px;color:var(--teal-dark)}
.partner{top:679px;width:98px;height:51px}

/* hello band */
.hello-band{left:0;top:750px;width:1200px;height:108px;background:var(--light);text-align:center}
.hello-band h2{font-size:14px;font-weight:700;margin-top:33px;color:var(--ink)}
.hello-band p{font-size:7.5px;color:var(--text-grey);margin-top:1px}
.social{display:flex;justify-content:center;gap:6px;margin-top:5px}
.social span{width:28px;height:11px;border-radius:1px}

/* footer */
.footer{left:0;top:858px;width:1200px;height:128px;background:var(--footer);border-top:2px solid var(--teal-dark)}
.footer-notch{left:597px;top:852px}
.footer-col{top:870px;color:var(--footer-text);font-size:7.5px;line-height:9.5px}
.footer-col h5{font-size:9px;font-weight:700;color:#e6e6e6;letter-spacing:.5px;margin-bottom:8px}
.footer-col p+p{margin-top:6px}
.portfolio-grid{display:grid;grid-template-columns:repeat(4,70px);grid-auto-rows:25px;gap:2px}
.contact-line{display:flex;align-items:center;gap:6px;margin-top:5px}
.bottom-bar{left:0;top:986px;width:1200px;height:14px;background:var(--footer-bottom);font-size:7.5px;color:var(--footer-text);line-height:14px}
.bottom-links{left:134px;top:0;display:flex}
.bottom-links span{padding:0 10px;border-right:1px solid #555}
.bottom-links span:first-child{padding-left:10px}
.bottom-links span:last-child{border:none}
.copyright{right:124px;top:0}
</style>
</head>
<body>

<header>
  <div class="abs top-rule"></div>
  <div class="abs brand">
    <span class="brand-mark"></span>
    <span class="brand-name">Oak Harbor Interiors</span>
  </div>
</header>

<section>
  <div class="abs hero-band"></div>
  <nav class="abs nav">
    <a class="active">HOME</a><a>PAGES</a><a>PORTFOLIO</a><a>PORTFOLIO CATEGORIES</a><a>SHOP</a><a>BLOG</a><a>GET IN TOUCH</a>
    <a class="cart"><svg width="10" height="8" viewBox="0 0 10 8"><path d="M0 1h2l1.5 4.5h5L10 2H3" fill="none" stroke="#1c4257" stroke-width="1.2"/><circle cx="4" cy="7" r=".9" fill="#1c4257"/><circle cx="8" cy="7" r=".9" fill="#1c4257"/></svg><span>0</span></a>
  </nav>
  <div class="abs search-btn"><svg width="9" height="9" viewBox="0 0 9 9"><circle cx="3.6" cy="3.6" r="2.6" fill="none" stroke="#fff" stroke-width="1.3"/><path d="M5.6 5.6 8.3 8.3" stroke="#fff" stroke-width="1.4"/></svg></div>
  <div class="abs slider" role="img" aria-label="Banner photo: two potted green plants in white planters against a turquoise wall on a pale wooden floor"></div>
  <div class="abs slider-title">LET YOUR HOME</div>
  <div class="abs slider-sub">Be unique and stylish</div>
  <div class="abs slider-dots"><span></span><span></span><span class="on"></span><span></span><span></span><span></span></div>
</section>

<p class="abs intro">Lorem Ipsum is simply dummy text of the printing and typesetting industry. Lorem Ipsum has been the industry's standard dummy text ever since the 1500</p>

<section>
  <div class="abs feature" style="left:138px">
    <div class="feature-badge"><svg width="52" height="18" viewBox="0 0 52 18" fill="#fff"><rect x="0" y="14" width="4" height="4"/><rect x="8" y="12" width="5" height="6"/><rect x="17" y="10" width="6" height="8"/><rect x="27" y="6" width="7" height="12"/><rect x="38" y="1" width="8" height="17"/></svg></div>
    <h3>LOREM IPSUM</h3>
    <p>Lorem Ipsum is simply dummy text of the printing and typesetting industry. Lorem Ipsum has been the industry's standard dummy text ever since the 1500s, when an unknown printer took a galley of type and scrambled.</p>
    <span class="btn">Read More</span>
  </div>
  <div class="abs feature" style="left:461px">
    <div class="feature-badge"><svg width="20" height="24" viewBox="0 0 20 24"><path d="M10 2a7 7 0 0 0-4 12.7V18h8v-3.3A7 7 0 0 0 10 2z" fill="none" stroke="#fff" stroke-width="2.2"/><rect x="7" y="19.5" width="6" height="2.5" fill="#fff"/></svg></div>
    <h3>LOREM IPSUM</h3>
    <p>Lorem Ipsum is simply dummy text of the printing and typesetting industry. Lorem Ipsum has been the industry's standard dummy text ever since the 1500s, when an unknown printer took a galley of type and scrambled.</p>
    <span class="btn">Read More</span>
  </div>
  <div class="abs feature" style="left:784px">
    <div class="feature-badge"><svg width="24" height="24" viewBox="0 0 24 24"><g fill="#fff"><circle cx="12" cy="12" r="7.5"/><rect x="10" y="1" width="4" height="22"/><rect x="1" y="10" width="22" height="4"/><rect x="10" y="1" width="4" height="22" transform="rotate(45 12 12)"/><rect x="10" y="1" width="4" height="22" transform="rotate(-45 12 12)"/></g><circle cx="12" cy="12" r="3.3" fill="#1c4257"/></svg></div>
    <h3>LOREM IPSUM</h3>
    <p>Lorem Ipsum is simply dummy text of the printing and typesetting industry. Lorem Ipsum has been the industry's standard dummy text ever since the 1500s, when an unknown printer took a galley of type and scrambled.</p>
    <span class="btn">Read More</span>
  </div>
</section>

<section>
  <h2 class="abs section-title" style="left:134px;top:466px">RECENT NEWS</h2>
  <div class="abs news-item" style="top:485px"><div class="thumb" role="img" aria-label="Interior photo thumbnail"></div><div><h4>Lorem ipsum dolor sit amet</h4><p>Lorem Ipsum is simply dummy text of the printing and typesetting industry.</p></div></div>
  <div class="abs news-item" style="top:515px"><div class="thumb" role="img" aria-label="Interior photo thumbnail" style="background:linear-gradient(90deg,#6f7883,#d9dde1)"></div><div><h4>Lorem ipsum dolor sit amet</h4><p>Lorem Ipsum is simply dummy text of the printing and typesetting industry.</p></div></div>
  <div class="abs news-item" style="top:545px"><div class="thumb" role="img" aria-label="Interior photo thumbnail" style="background:linear-gradient(90deg,#8e8a86,#dedbd6)"></div><div><h4>Lorem ipsum dolor sit amet</h4><p>Lorem Ipsum is simply dummy text of the printing and typesetting industry.</p></div></div>
  <div class="abs news-item" style="top:575px"><div class="thumb" role="img" aria-label="Interior photo thumbnail" style="background:linear-gradient(90deg,#5a4f47,#cfc6bc)"></div><div><h4>Lorem ipsum dolor sit amet</h4><p>Lorem Ipsum is simply dummy text of the printing and typesetting industry.</p></div></div>
  <span class="abs btn btn-dark" style="left:134px;top:604px">View More</span>

  <h2 class="abs section-title" style="left:474px;top:466px">FRESH <em>UNIQUE</em> DESIGNS</h2>
  <div class="abs gallery" role="img" aria-label="Gallery of twelve interior design project photos: living rooms, bedrooms and kitchens">
    <div style="background:linear-gradient(135deg,#e9ecef,#9ea6ad)"></div>
    <div style="background:linear-gradient(180deg,#d9dcdf,#2c2c2c)"></div>
    <div style="background:linear-gradient(135deg,#5b4a3e,#d8cfc6)"></div>
    <div style="background:linear-gradient(180deg,#f2f2f2,#4a3527)"></div>
    <div style="background:linear-gradient(180deg,#d8cdb8,#c07a2e)"></div>
    <div style="background:linear-gradient(135deg,#6b5a4c,#e6e2dc)"></div>
    <div style="background:linear-gradient(180deg,#e6e6e4,#a9adb0)"></div>
    <div style="background:linear-gradient(180deg,#f4f4f4,#c7cbd0)"></div>
    <div style="background:linear-gradient(180deg,#b9c6d3,#7a5a3b)"></div>
    <div style="background:linear-gradient(135deg,#dfe1e3,#2a2a2a)"></div>
    <div style="background:linear-gradient(135deg,#f3f3f3,#262626)"></div>
    <div style="background:linear-gradient(135deg,#e4e6e8,#3a3d40)"></div>
  </div>
  <span class="abs btn btn-dark" style="left:474px;top:627px">View More</span>
</section>

<section>
  <h2 class="abs section-title" style="left:135px;top:660px">Testimonial</h2>
  <div class="abs testimonial-photo" role="img" aria-label="Portrait photo of the client giving the testimonial"></div>
  <blockquote class="abs quote">Lorem Ipsum is simply dummy text of the printing and typesetting industry. Lorem Ipsum has been the industry's standard dummy text ever since the 1500</blockquote>
  <span class="abs quote-author">Lorem ipsum</span>

  <h2 class="abs section-title" style="left:620px;top:660px">OUR <em>PARTNERS</em></h2>
  <div class="abs partner" style="left:634px;background:linear-gradient(135deg,#5a3a28,#d9b59a)" role="img" aria-label="Portrait photo of a partner"></div>
  <div class="abs partner" style="left:749px;background:linear-gradient(135deg,#e4e4e4,#3a2c24)" role="img" aria-label="Portrait photo of a partner"></div>
  <div class="abs partner" style="left:864px;background:linear-gradient(135deg,#f0eeee,#c39a6e)" role="img" aria-label="Portrait photo of a partner"></div>
  <div class="abs partner" style="left:979px;background:linear-gradient(135deg,#b9b6b2,#2e2c2c)" role="img" aria-label="Portrait photo of a partner"></div>
</section>

<section class="abs hello-band">
  <h2>HELLO !</h2>
  <p>Lorem Ipsum is simply dummy text of the printing and typesetting industry. Lorem Ipsum has been the industry's standard dummy text ever since the 1500</p>
  <div class="social">
    <span style="background:#3b5a9a"></span>
    <span style="background:#6aa82c"></span>
    <span style="background:#29a8e0"></span>
    <span style="background:#e4502f"></span>
    <span style="background:#2fa6dd"></span>
  </div>
</section>

<footer>
  <div class="abs footer"></div>
  <svg class="abs footer-notch" width="16" height="7" viewBox="0 0 16 7"><path d="M0 7 8 0l8 7z" fill="#1c4257"/></svg>

  <div class="abs footer-col" style="left:135px;width:290px">
    <h5>ABOUT !</h5>
    <p>Lorem Ipsum is simply dummy text of the printing and typesetting industry. Lorem Ipsum has been the industry's standard dummy text ever since the 1500s, when an unknown printer took a galley of type and scrambled</p>
    <p>It to make a type specimen book. It has survived not only five centuries, but also the leap into electronic typesetting, remaining essentially</p>
  </div>

  <div class="abs footer-col" style="left:460px">
    <h5>RECENT PORTFOLIO</h5>
    <div class="portfolio-grid" role="img" aria-label="Twelve small photos of recent interior portfolio projects">
      <div style="background:#9aa7ad"></div><div style="background:#4b5c6d"></div><div style="background:#7f8a8e"></div><div style="background:#3a3532"></div>
      <div style="background:#8e9a8c"></div><div style="background:#8c6a3e"></div><div style="background:#d4d4d2"></div><div style="background:#b6b4ae"></div>
      <div style="background:#5f6e78"></div><div style="background:#a8a39b"></div><div style="background:#c9cbcc"></div><div style="background:#8d9499"></div>
    </div>
  </div>

  <div class="abs footer-col" style="left:788px;width:270px">
    <h5>CONTACT INFO</h5>
    <p>Etiam vitae convallis dui. Proin vitae felis magna. Morbi dui quam, faucibus at nulla sed, ullamcorper consectetur velit.</p>
    <div class="contact-line"><svg width="9" height="9" viewBox="0 0 9 9"><path d="M1.5 1 3.3.6 4.2 2.8 3.1 3.6a5 5 0 0 0 2.3 2.3l.8-1.1 2.2.9-.4 1.8C5 7.7 1.3 4 1.5 1z" fill="#8d8d8d"/></svg><span>000-000-0000</span></div>
    <div class="contact-line"><svg width="9" height="9" viewBox="0 0 9 9"><rect x="1" y="3" width="7" height="4" fill="none" stroke="#8d8d8d"/><rect x="2.5" y="1" width="4" height="2" fill="#8d8d8d"/></svg><span>000-000-0000</span></div>
    <div class="contact-line"><svg width="9" height="9" viewBox="0 0 9 9"><rect x=".7" y="2" width="7.6" height="5.2" fill="none" stroke="#8d8d8d"/><path d="m.7 2 3.8 3 3.8-3" fill="none" stroke="#8d8d8d"/></svg><span>Lorem@gmail.com</span></div>
    <div class="contact-line"><svg width="9" height="9" viewBox="0 0 9 9"><path d="M4.5 1 .8 4.3h1.1V8h2V6h1.2v2h2V4.3h1.1z" fill="#8d8d8d"/></svg><span>00 Lorem ipsum dolor, Lorem, Ll 00000000</span></div>
  </div>

  <div class="abs bottom-bar">
    <div class="abs bottom-links"><span>ABOUT US</span><span>SERVICES</span><span>BLOG</span><span>GET IN TOUCH</span></div>
    <div class="abs copyright">© Copyright 2014. All right reserved.</div>
  </div>
</footer>

</body>
</html>
```